Professional
Mark Elwood
President
4217 Vista Arroyo Place, NW
Albuquerque, NM 87114
melwood@emibq.com
www.emibq.com
New Construction*Remodels* Renovations*Handyman Services
Here is my logo for the stationary and business cards
Logo .AI file

```html
<!DOCTYPE html>
<html lang="en">
<head>
<meta charset="utf-8">
<title>Elwood Masonry, Inc — Business Card</title>
<link rel="stylesheet" href="https://fonts.googleapis.com/css2?family=Arimo:wght@400;700&display=swap">
<style>
  :root {
    --backdrop: #e9e6e2;
    --card: #ffffff;
    --brand-red: #e11b22;
    --ink: #111111;
    --body-text: #4a4a4a;
    --rule: #d6d6d6;
  }
  * { margin: 0; padding: 0; box-sizing: border-box; }
  html, body { width: 1200px; height: 780px; overflow: hidden; }
  body {
    background: var(--backdrop);
    font-family: "Arimo", Arial, sans-serif;
    position: relative;
  }
  .business-card {
    position: absolute;
    left: 80px; top: 85px;
    width: 1040px; height: 610px;
    background: var(--card);
    border-radius: 44px;
    overflow: hidden;
    box-shadow: 0 6px 18px rgba(0,0,0,0.18);
  }
  .edge-band {
    position: absolute; left: 0; top: 0; bottom: 0;
    width: 34px; background: var(--brand-red);
  }
  .edge-line {
    position: absolute; left: 40px; top: 0; bottom: 0;
    width: 5px; background: var(--ink);
  }
  .brand {
    position: absolute; left: 110px; top: 255px;
    display: flex; align-items: center; gap: 18px;
  }
  .brand-mark {
    width: 96px; height: 96px; border-radius: 50%;
    background: var(--brand-red);
  }
  .brand-text { display: flex; flex-direction: column; }
  .brand-name {
    font-weight: 700; font-size: 38px; color: var(--ink);
    letter-spacing: 1px; line-height: 1.05;
  }
  .brand-tagline {
    font-size: 13px; color: var(--body-text); margin-top: 6px;
  }
  .divider {
    position: absolute; left: 565px; top: 40px; bottom: 40px;
    width: 2px; background: var(--rule);
  }
  .contact {
    position: absolute; left: 600px; top: 52px;
    color: var(--body-text); font-size: 24px; line-height: 1.35;
  }
  .contact-name { color: var(--brand-red); font-weight: 700; font-size: 34px; }
  .contact-title { color: var(--ink); font-weight: 700; font-size: 24px; margin-bottom: 44px; }
  .address { margin-bottom: 26px; }
  .detail-row { display: flex; align-items: center; gap: 12px; }
  .detail-row svg { width: 22px; height: 22px; flex: none; }
  .license { margin-left: 0; }
</style>
</head>
<body>
  <main class="business-card">
    <div class="edge-band"></div>
    <div class="edge-line"></div>

    <div class="brand">
      <div class="brand-mark"></div>
      <div class="brand-text">
        <span class="brand-name">ELWOOD</span>
        <span class="brand-name">MASONRY, INC</span>
        <span class="brand-tagline">Remodels and Renovations</span>
      </div>
    </div>

    <div class="divider"></div>

    <section class="contact">
      <div class="contact-name">Mark Elwood</div>
      <div class="contact-title">President</div>
      <div class="address">4217 Vista Arroyo Place, NW<br>Albuquerque, NM 87114</div>
      <div class="license">Lic no : 482917</div>
      <div class="detail-row">
        <svg viewBox="0 0 24 24" aria-hidden="true"><rect x="7" y="2" width="10" height="20" rx="2" fill="#e11b22"/><rect x="9" y="5" width="6" height="9" fill="#fff"/></svg>
        <span>505-555-0182</span>
      </div>
      <div class="detail-row">
        <svg viewBox="0 0 24 24" aria-hidden="true"><path d="M4 9c0-3 16-3 16 0l-3 2-2-2H9l-2 2z M6 13h12v8H6z" fill="#e11b22"/></svg>
        <span>505-555-0147</span>
      </div>
      <div class="detail-row">
        <svg viewBox="0 0 24 24" aria-hidden="true"><circle cx="12" cy="12" r="8" fill="none" stroke="#e11b22" stroke-width="3"/><circle cx="12" cy="12" r="3" fill="#e11b22"/></svg>
        <span>melwood@emibq.com</span>
      </div>
      <div class="detail-row">
        <svg viewBox="0 0 24 24" aria-hidden="true"><circle cx="12" cy="12" r="9" fill="none" stroke="#e11b22" stroke-width="2"/><path d="M3 12h18M12 3c4 4 4 14 0 18M12 3c-4 4-4 14 0 18" fill="none" stroke="#e11b22" stroke-width="1.5"/></svg>
        <span>www.emibq.com</span>
      </div>
    </section>
  </main>
</body>
</html>
```